Horse Training Trade Show Stand

We're looking to redo our Trade Show backdrop to suit our newer approach to business.

We're an online horse training company, specializing in videos and podcasts. The backdrop will be used at events to capture people's attention and immediately get people to understand who we are and what we do.

We want to change up our vibe. We want to have a more minimalist feel.

Think all of those simple websites with sans serif text.
Think Plumwick.com type of text and feel.

We also want to update our colors. Traditionally we have used Tans and Browns. We want to move to do something more Blue, Brown, and White.

Attached are various previous designs for our past booth designs. I have also attached the PDF template of the background and provided various pictures and logos to use wherever seen fit.

I have also attached some of our printed ads so you can get a feel for what our brand is and says. Again, we're looking to change the feel and vibe. But it'll give you context.

Target Market(s)

Women 30-60

Industry/Entity Type

Education

Font styles to use
Sans Serif

Colors
0054AA
0677BA
7BADD7
CADEEF
E8F1F8

Requirements
Must have
• Logo
Nice to have
• Eye-catching shapes

```html
<!DOCTYPE html>
<html lang="en">
<head>
<meta charset="utf-8">
<title>Hollis Creek – Trade Show Backdrop</title>
<link href="https://fonts.googleapis.com/css2?family=Oswald:wght@500;600&family=Montserrat:wght@500;600&display=swap" rel="stylesheet">
<style>
  :root{
    --page:#e9e9e9;
    --white:#ffffff;
    --brown-light:#7a5242;
    --brown-dark:#4b2f24;
    --cream:#f4e7a6;
    --blue-deep:#0054AA;
    --blue-mid:#0677BA;
    --blue-bright:#1a8ddc;
    --ink:#1f1f1f;
  }
  html,body{margin:0;padding:0;width:723px;height:1200px;overflow:hidden;background:var(--page);}
  .backdrop{position:absolute;left:0;top:239px;width:723px;height:722px;display:block;}
  .headline{font-family:'Oswald',sans-serif;font-weight:600;fill:var(--white);font-size:31px;letter-spacing:.5px;}
  .subline{font-family:'Oswald',sans-serif;font-weight:500;fill:var(--brown-dark);font-size:17px;letter-spacing:.4px;}
  .brand-name{font-family:'Oswald',sans-serif;font-weight:600;fill:var(--white);font-size:22px;letter-spacing:1px;}
  .brand-tag{font-family:'Montserrat',sans-serif;font-weight:500;fill:var(--white);font-size:8px;letter-spacing:.5px;}
  .phone{font-family:'Oswald',sans-serif;font-weight:500;fill:var(--ink);font-size:18px;}
  .web{font-family:'Montserrat',sans-serif;font-weight:500;fill:var(--white);font-size:11.5px;}
  .divider{fill:none;stroke:var(--white);stroke-width:9;stroke-linejoin:miter;}
</style>
</head>
<body>
<svg class="backdrop" viewBox="0 0 736 735" xmlns="http://www.w3.org/2000/svg">
  <defs>
    <linearGradient id="greenery" x1="0" y1="0" x2="0" y2="1">
      <stop offset="0" stop-color="#6f9140"/><stop offset="1" stop-color="#a9b06a"/>
    </linearGradient>
    <linearGradient id="paddock" x1="0" y1="0" x2="0" y2="1">
      <stop offset="0" stop-color="#d7e3ec"/><stop offset=".55" stop-color="#b59078"/><stop offset="1" stop-color="#d8d2c8"/>
    </linearGradient>
    <linearGradient id="sunset" x1="0" y1="0" x2="0" y2="1">
      <stop offset="0" stop-color="#f3e7a2"/><stop offset=".45" stop-color="#e9c15a"/><stop offset=".7" stop-color="#2a2218"/><stop offset="1" stop-color="#111"/>
    </linearGradient>
    <linearGradient id="arena" x1="0" y1="0" x2="0" y2="1">
      <stop offset="0" stop-color="#ece9e4"/><stop offset=".6" stop-color="#c8a27e"/><stop offset="1" stop-color="#e6e2dc"/>
    </linearGradient>
    <linearGradient id="brownPanel" x1="0" y1="0" x2="0" y2="1">
      <stop offset="0" stop-color="var(--brown-light)"/><stop offset="1" stop-color="var(--brown-dark)"/>
    </linearGradient>
    <linearGradient id="bluePanel" x1="0" y1="0" x2="1" y2="0">
      <stop offset="0" stop-color="var(--blue-deep)"/><stop offset=".6" stop-color="var(--blue-mid)"/><stop offset="1" stop-color="var(--blue-bright)"/>
    </linearGradient>
    <clipPath id="hexClip"><polygon points="176,245 366,150 560,245 560,490 366,572 176,490"/></clipPath>
  </defs>

  <g class="photo-top" role="img" aria-label="Photo of a bay horse and a trainer in a cowboy hat against green trees">
    <polygon points="0,0 736,0 736,150 560,245 366,150 176,245 0,150" fill="url(#greenery)"/>
  </g>
  <g class="photo-left" role="img" aria-label="Photo of a trainer standing beside a paint horse at a fence">
    <polygon points="0,150 176,245 176,490 0,578" fill="url(#paddock)"/>
  </g>
  <g class="photo-right" role="img" aria-label="Silhouette of a rider and horse at sunset">
    <polygon points="736,150 560,245 560,490 736,578" fill="url(#sunset)"/>
  </g>
  <g class="photo-bottom" role="img" aria-label="Photo of a trainer sitting in the arena with a chestnut foal">
    <polygon points="0,578 176,490 366,572 560,490 736,578 736,735 0,735" fill="url(#arena)"/>
  </g>

  <g class="center-panel" clip-path="url(#hexClip)">
    <rect x="170" y="140" width="400" height="237" fill="url(#brownPanel)"/>
    <rect x="170" y="377" width="400" height="30" fill="var(--cream)"/>
    <rect x="170" y="407" width="400" height="170" fill="url(#bluePanel)"/>
  </g>

  <polyline class="divider" points="0,150 176,245 366,150 560,245 736,150"/>
  <polyline class="divider" points="0,578 176,490 366,572 560,490 736,578"/>
  <line class="divider" x1="176" y1="241" x2="176" y2="494"/>
  <line class="divider" x1="560" y1="241" x2="560" y2="494"/>

  <text class="headline" x="366" y="322" text-anchor="middle">WE'RE AN ONLINE HORSE</text>
  <text class="headline" x="366" y="360" text-anchor="middle">TRAINING COMPANY</text>
  <text class="subline" x="366" y="399" text-anchor="middle">SPECIALIZING IN VIDEOS AND PODCASTS.</text>

  <text class="brand-name" x="366" y="448" text-anchor="middle">HOLLIS CREEK</text>
  <text class="brand-tag" x="366" y="463" text-anchor="middle">Steady Horsemanship</text>

  <g class="phone-pill">
    <rect x="286" y="481" width="170" height="25" rx="12.5" fill="var(--white)"/>
    <circle cx="301" cy="493.5" r="8" fill="var(--ink)"/>
    <path d="M297.5 489.5 q0.5-1 1.5-.8 l1.2 2 -.9 .9 q.8 1.8 2.3 2.6 l.9-.9 2 1.2 q.2 1-.8 1.5 q-3.6 .3-6.2-6.5z" fill="var(--white)"/>
    <text class="phone" x="313" y="500">+1 555-014-0282</text>
  </g>
  <text class="web" x="366" y="523" text-anchor="middle">www.holliscreek.com</text>
</svg>
</body>
</html>
```